Camp Thornbrake "The '63 Circle"

We are looking for someone to design a bi-fold brochure that will help with our fundraising program. We are a Christian camp and retreat center. It would be a good idea to visit our website to get a feel for what we do, campthornbrake.org.

This link, https://files.exampleshare.net/folders/9KxTb3RmQa7VzLp2NcHw5YdFs8GjUe4Xo?usp=sharing, will provide you with pictures you can use and the text that will be needed. Don't expect all the pictures to be used, but wanted to provide some choices. The text that is provided will need to be used on the inside portion of the brochure.

Target Market(s)

Donors age range 25-70

Industry/Entity Type

Recreation

Requirements
Must have
• Text included in Google Drive. A few pictures. Thornbrake Logo
Nice to have
• Professional Design
Should not have
• No clip art, no extra text (even from the website)

```html
<!DOCTYPE html>
<html lang="en">
<head>
<meta charset="utf-8">
<title>Camp Thornbrake – The '63 Circle Brochure</title>
<link href="https://fonts.googleapis.com/css2?family=Bebas+Neue&family=Open+Sans:ital,wght@0,400;0,600;0,700;1,400&display=swap" rel="stylesheet">
<style>
  :root {
    --backdrop: #e4e4e4;
    --paper: #f7f7f7;
    --green: #1b6b4b;
    --orange: #e9a15a;
    --ink: #1e1e1e;
    --body: #4a4a4a;
    --ring: #cfcfcf;
    --fold: rgba(0,0,0,0.08);
  }
  * { box-sizing: border-box; margin: 0; padding: 0; }
  html, body { width: 1200px; height: 2315px; overflow: hidden; }
  body { background: var(--backdrop); font-family: "Open Sans", Arial, sans-serif; color: var(--body); position: relative; }

  .page {
    position: absolute; width: 500px; height: 707px;
    background: var(--paper); overflow: hidden;
    box-shadow: 0 10px 30px rgba(0,0,0,0.12);
  }
  .spread-left { box-shadow: inset -18px 0 22px -18px var(--fold), 0 10px 30px rgba(0,0,0,0.12); }
  .spread-right { box-shadow: inset 18px 0 22px -18px var(--fold), 0 10px 30px rgba(0,0,0,0.12); }

  .photo-circle { position: absolute; display: block; }

  .brand {
    position: absolute; top: 70px; right: 34px;
    display: flex; align-items: center; gap: 8px;
  }
  .brand-dot { width: 14px; height: 14px; border-radius: 50%; background: var(--green); }
  .brand-name { font-family: "Bebas Neue", Impact, sans-serif; font-size: 24px; color: var(--ink); letter-spacing: 0.5px; }

  .cover-title {
    position: absolute; left: 34px; bottom: 62px;
    font-family: "Bebas Neue", Impact, sans-serif; color: var(--ink);
    font-size: 44px; line-height: 0.95; letter-spacing: 1px;
  }
  .cover-title .line-one { display: block; padding-left: 118px; }
  .cover-title .line-two { display: block; }

  .section-heading {
    font-family: "Bebas Neue", Impact, sans-serif; color: var(--ink);
    font-size: 26px; letter-spacing: 1px; display: inline-block;
    border-bottom: 2px solid var(--ink); padding-bottom: 1px; line-height: 1;
  }
  .about { position: absolute; left: 44px; top: 44px; width: 412px; }
  .about p, .mission p {
    font-size: 11.2px; line-height: 1.55; text-align: justify; margin-top: 12px;
  }
  .mission { position: absolute; left: 44px; top: 336px; width: 420px; }
  .mission p:first-child { margin-top: 0; }

  .contact { position: absolute; left: 0; right: 0; top: 340px; text-align: center; }
  .contact-list { list-style: none; margin-top: 18px; }
  .contact-list li {
    display: flex; flex-direction: column; align-items: center; gap: 4px;
    font-size: 12px; color: var(--ink); margin-bottom: 10px;
  }
  .contact-list .phone { font-weight: 700; color: var(--green); font-size: 16px; }
  .icon { width: 16px; height: 16px; display: block; }
</style>
</head>
<body>

<!-- Row 1: front cover -->
<section class="page" style="left:350px; top:40px;" aria-label="Front cover">
  <svg class="photo-circle" style="left:98px; top:58px;" width="390" height="390" viewBox="0 0 390 390">
    <defs>
      <linearGradient id="g-cover-a" x1="0" y1="0" x2="1" y2="1">
        <stop offset="0" stop-color="#3f6b3a"/><stop offset="0.55" stop-color="#3a4f8a"/><stop offset="1" stop-color="#9b3b3d"/>
      </linearGradient>
    </defs>
    <circle cx="195" cy="195" r="188" fill="none" stroke="var(--ring)" stroke-width="1.2"/>
    <circle cx="195" cy="195" r="163" fill="none" stroke="var(--green)" stroke-width="16" stroke-dasharray="840 1024" transform="rotate(60 195 195)"/>
    <circle cx="195" cy="195" r="152" fill="url(#g-cover-a)" role="img" aria-label="Photo of campers in life jackets smiling together outdoors"/>
  </svg>
  <div class="brand"><span class="brand-dot"></span><span class="brand-name">Camp Thornbrake</span></div>
  <h1 class="cover-title"><span class="line-one">Christian Camp</span><span class="line-two">And Retreat Center Facility</span></h1>
</section>

<!-- Row 2: inside spread -->
<section class="page spread-left" style="left:80px; top:800px;" aria-label="Inside left page">
  <div class="about">
    <h2 class="section-heading">About Thornbrake</h2>
    <p>Camp Thornbrake was established in 1948 by Walter &amp; Edna Hollis and many other families to provide a place where children would have the opportunity to Encounter Christ, Community &amp; Creation. The founders of Thornbrake wanted to provide a great experience at a reasonable price.</p>
    <p>We are committed to continuing that same core value. We don't believe that an incredible camp experience should only be for kids who can afford an incredible camp experience. We believe strongly that Christian Camping is a great mission field where lives are changed forever.</p>
  </div>
  <svg class="photo-circle" style="left:30px; top:330px;" width="240" height="240" viewBox="0 0 240 240">
    <defs>
      <linearGradient id="g-foam" x1="0" y1="0" x2="1" y2="1">
        <stop offset="0" stop-color="#4b5566"/><stop offset="0.5" stop-color="#b9bfca"/><stop offset="1" stop-color="#3c4658"/>
      </linearGradient>
    </defs>
    <circle cx="120" cy="120" r="116" fill="none" stroke="var(--ring)" stroke-width="1.2"/>
    <circle cx="120" cy="120" r="100" fill="none" stroke="var(--green)" stroke-width="12" stroke-dasharray="520 628" transform="rotate(60 120 120)"/>
    <circle cx="120" cy="120" r="92" fill="url(#g-foam)" role="img" aria-label="Photo of campers covered in foam during a messy game"/>
  </svg>
  <svg class="photo-circle" style="left:196px; top:528px;" width="132" height="132" viewBox="0 0 132 132">
    <defs>
      <linearGradient id="g-pool" x1="0" y1="0" x2="1" y2="1">
        <stop offset="0" stop-color="#2e3f5a"/><stop offset="1" stop-color="#56b6d6"/>
      </linearGradient>
    </defs>
    <circle cx="66" cy="66" r="63" fill="none" stroke="var(--ring)" stroke-width="1.2"/>
    <circle cx="66" cy="66" r="53" fill="none" stroke="var(--orange)" stroke-width="8" stroke-dasharray="270 333" transform="rotate(60 66 66)"/>
    <circle cx="66" cy="66" r="48" fill="url(#g-pool)" role="img" aria-label="Photo of campers gathered in a swimming pool"/>
  </svg>
</section>

<section class="page spread-right" style="left:620px; top:800px;" aria-label="Inside right page">
  <svg class="photo-circle" style="left:118px; top:-110px;" width="420" height="420" viewBox="0 0 420 420">
    <defs>
      <linearGradient id="g-trail" x1="0" y1="0" x2="1" y2="1">
        <stop offset="0" stop-color="#2f5a2c"/><stop offset="0.6" stop-color="#7c8f5c"/><stop offset="1" stop-color="#d9c8a3"/>
      </linearGradient>
    </defs>
    <circle cx="210" cy="210" r="208" fill="var(--orange)"/>
    <circle cx="210" cy="200" r="198" fill="url(#g-trail)" role="img" aria-label="Photo of counselor and young campers walking on a wooded path"/>
  </svg>
  <div class="mission">
    <p>It cost Thornbrake just over $500 for a one-week camper and around $800 for a two-week camper. We currently charge $285 for a one-week session and $425 for a two-week session. These gaps create a significant budget shortfall each year that must be filled with both alternative revenue streams and fundraising, which makes it challenging to also raise money to make improvements to our camp facilities.</p>
    <p>In an effort to keep camper fees at a reasonable level we established The '63 Circle. Members of The '63 Circle are former campers, counselors and families that have been impacted by the ministry of Thornbrake. They believe in the mission of Christian camping. By providing monthly support they help to defray some of the cost for campers, which allows more children to attend Thornbrake each summer and facility updates.</p>
    <p>We hope you will consider joining this effort. Recurring donations can be set up at campthornbrake.org by clicking on the “Give Now” button at the top of the page and selecting the subaccount “The '63 Circle.” Be sure to choose your recurring date before clicking in the “submit” button. Checks can be mailed to P.O. Box 702, Millbrook, AR 72001.</p>
  </div>
</section>

<!-- Row 3: back and front covers -->
<section class="page spread-left" style="left:80px; top:1570px;" aria-label="Back cover">
  <svg class="photo-circle" style="left:20px; top:-150px;" width="440" height="440" viewBox="0 0 440 440">
    <defs>
      <linearGradient id="g-cabin" x1="0" y1="0" x2="1" y2="1">
        <stop offset="0" stop-color="#7a3a2e"/><stop offset="0.5" stop-color="#5a5f7a"/><stop offset="1" stop-color="#8a2f26"/>
      </linearGradient>
    </defs>
    <circle cx="220" cy="220" r="218" fill="var(--orange)"/>
    <circle cx="220" cy="208" r="206" fill="url(#g-cabin)" role="img" aria-label="Photo of a group of girls posing in front of a red cabin"/>
  </svg>
  <div class="contact">
    <h2 class="section-heading">Contact Us</h2>
    <ul class="contact-list">
      <li>
        <svg class="icon" viewBox="0 0 16 16"><circle cx="8" cy="8" r="8" fill="var(--green)"/><path d="M5.2 4.2l1.4-.4.9 2-.9.7c.4.9 1 1.6 1.9 2.1l.7-.9 2 .9-.4 1.4c-3 .1-5.7-2.7-5.6-5.8z" fill="#fff"/></svg>
        <span class="phone">555-014-2288</span>
      </li>
      <li>
        <svg class="icon" viewBox="0 0 16 16"><circle cx="8" cy="8" r="8" fill="var(--green)"/><rect x="4" y="5" width="8" height="6" fill="none" stroke="#fff" stroke-width="1"/><path d="M4 5l4 3.2L12 5" fill="none" stroke="#fff" stroke-width="1"/></svg>
        <span>office@campthornbrake.org</span>
      </li>
      <li>
        <svg class="icon" viewBox="0 0 16 16"><circle cx="8" cy="8" r="8" fill="var(--green)"/><path d="M8 12.5S5 9.2 5 7a3 3 0 016 0c0 2.2-3 5.5-3 5.5z" fill="#fff"/><circle cx="8" cy="7" r="1.1" fill="var(--green)"/></svg>
        <span>48 Cedar Hollow Road Millbrook, AR 72000</span>
      </li>
      <li>
        <svg class="icon" viewBox="0 0 16 16"><circle cx="8" cy="8" r="8" fill="var(--green)"/><circle cx="8" cy="8" r="3.6" fill="none" stroke="#fff" stroke-width="1"/><path d="M4.4 8h7.2M8 4.4c-1.6 2.2-1.6 5 0 7.2M8 4.4c1.6 2.2 1.6 5 0 7.2" fill="none" stroke="#fff" stroke-width="0.8"/></svg>
        <span>www.campthornbrake.org</span>
      </li>
    </ul>
  </div>
</section>

<section class="page spread-right" style="left:620px; top:1570px;" aria-label="Front cover">
  <svg class="photo-circle" style="left:98px; top:58px;" width="390" height="390" viewBox="0 0 390 390">
    <defs>
      <linearGradient id="g-cover-b" x1="0" y1="0" x2="1" y2="1">
        <stop offset="0" stop-color="#3f6b3a"/><stop offset="0.55" stop-color="#3a4f8a"/><stop offset="1" stop-color="#9b3b3d"/>
      </linearGradient>
    </defs>
    <circle cx="195" cy="195" r="188" fill="none" stroke="var(--ring)" stroke-width="1.2"/>
    <circle cx="195" cy="195" r="163" fill="none" stroke="var(--green)" stroke-width="16" stroke-dasharray="840 1024" transform="rotate(60 195 195)"/>
    <circle cx="195" cy="195" r="152" fill="url(#g-cover-b)" role="img" aria-label="Photo of campers in life jackets smiling together outdoors"/>
  </svg>
  <div class="brand"><span class="brand-dot"></span><span class="brand-name">Camp Thornbrake</span></div>
  <h1 class="cover-title"><span class="line-one">Christian Camp</span><span class="line-two">And Retreat Center Facility</span></h1>
</section>

</body>
</html>
```